use the existing webpage www.lorvanbeauty.ch an create a modern style page using the same logos pictures and text . t
Target Market(s)
healthcare and cosmetigs
Number of Pages Required
1 page
Requirements
Must have
- same cooperate identity and style as the original lorvanbeauty.ch
- a link to the webshop: https://www.lorvanbeauty.shopnest.ch/ (no new window)
- ignore evntual text written in polish language.

```html
<!DOCTYPE html>
<html lang="en">
<head>
<meta charset="utf-8">
<title>Lorvan Beauty – Eyelash Serum</title>
<link rel="stylesheet" href="https://fonts.googleapis.com/css2?family=Cinzel:wght@400;600&family=Open+Sans:wght@400;600&display=swap">
<style>
:root{
  --ink:#1b1b1b;
  --header:#161616;
  --gold:#b59c63;
  --gold-light:#d9c596;
  --gold-dark:#86703f;
  --button:#7b6739;
  --grey-dark:#3a3a3a;
  --paper:#ffffff;
  --muted:#555;
}
*{box-sizing:border-box;margin:0;padding:0}
html,body{width:1200px;height:2952px;overflow:hidden}
body{font-family:"Open Sans",Arial,sans-serif;color:var(--ink);background:var(--paper);position:relative}
a{color:inherit;text-decoration:none}
.section{position:absolute;left:0;width:1200px}
.btn{display:inline-block;background:var(--button);color:#fff;font-size:15px;font-weight:600;padding:13px 30px;border-radius:2px}
.heading{font-family:"Cinzel",Georgia,serif;font-weight:400;line-height:1.15}
.body-text{font-size:14px;line-height:1.6;color:var(--muted)}

/* header */
.site-header{top:0;height:60px;background:var(--header);display:flex;align-items:center;justify-content:space-between;padding:0 40px;z-index:3}
.brand{font-family:"Open Sans",Arial,sans-serif;font-weight:600;color:#fff;font-size:16px}
.main-nav{display:flex;gap:26px;align-items:center;color:#fff;font-size:14px}
.main-nav .active{border-bottom:2px solid var(--gold);padding-bottom:3px}
.flags{display:flex;gap:6px}
.flags span{width:18px;height:12px;display:block}

/* hero */
.hero{top:60px;height:660px;overflow:hidden;background:linear-gradient(90deg,#f4f4f4 0%,#e9e9e9 45%,#9a9a9a 75%,#5a5a5a 100%)}
.hero-photo{position:absolute;right:0;top:0;width:640px;height:660px;background:radial-gradient(ellipse at 55% 40%,#cfcfcf 0%,#8d8d8d 45%,#3e3e3e 100%)}
.hero-copy{position:absolute;left:124px;top:185px;width:410px}
.hero-copy .heading{font-size:44px;color:var(--ink)}
.hero-copy .heading span{display:block;font-size:60px}
.hero-copy .body-text{color:#333;margin:18px 0 28px;font-size:15px}
.slider-dots{position:absolute;left:560px;top:525px;display:flex;gap:9px;z-index:2}
.slider-dots i{width:11px;height:11px;border-radius:50%;background:#555;display:block}
.slider-dots i.on{background:#111}
.hero-curve{position:absolute;left:0;bottom:0}

/* serum intro */
.serum-intro{top:720px;height:390px}
.serum-portrait{position:absolute;left:350px;top:20px;width:250px;height:250px;border-radius:50%;background:radial-gradient(circle at 45% 40%,#9c9c9c,#2b2b2b 70%,#111)}
.serum-copy{position:absolute;left:660px;top:30px;width:470px}
.serum-copy .heading{font-size:24px;font-weight:600}
.serum-copy .body-text{margin:16px 0 22px;font-size:13px;width:420px}

/* product bands */
.product-band{overflow:hidden}
.product-band .copy{position:absolute;width:460px}
.product-band .heading{font-size:36px;font-weight:600}
.product-band .label{font-size:14px;font-weight:600;margin-top:10px;letter-spacing:1px}
.product-band .body-text{font-size:13px;margin:14px 0 30px}
.product-shot{position:absolute}
.band-gold{top:1110px;height:390px;background:linear-gradient(90deg,#f1e6cb 0%,var(--gold-light) 35%,var(--gold) 65%,var(--gold-dark) 100%)}
.band-gold .copy{left:130px;top:115px}
.band-white{top:1520px;height:450px;background:var(--paper)}
.band-white .copy{left:640px;top:95px}
.band-grey{top:2010px;height:460px;background:linear-gradient(90deg,var(--grey-dark) 0%,#5c5c5c 45%,#b5b5b5 100%)}
.band-grey .copy{left:150px;top:120px}
.band-grey .heading,.band-grey .body-text{color:#fff}
.band-grey .btn{background:#333}

/* newsletter */
.newsletter{top:2470px;height:140px;display:flex;align-items:center;justify-content:center;gap:40px}
.newsletter .heading{font-size:30px;letter-spacing:1px}
.subscribe-form{display:flex;align-items:center;border:1px solid #bbb;border-radius:22px;width:520px;height:40px;padding-left:14px;gap:10px}
.subscribe-form .field{flex:1;font-size:13px;color:#777}
.subscribe-form .send{background:var(--button);color:#fff;font-size:13px;height:38px;line-height:38px;padding:0 28px;border-radius:20px}

/* footer */
.site-footer{top:2610px;height:295px;background:linear-gradient(90deg,#a98f57,var(--gold) 50%,#9c8451);color:#fff;padding:50px 140px 0;display:flex;gap:90px}
.footer-col h4{font-family:"Cinzel",Georgia,serif;font-weight:400;font-size:22px;margin-bottom:14px}
.footer-col li{list-style:none;font-size:14px;line-height:1.75}
.contact-field{width:190px;border-bottom:1px solid rgba(255,255,255,.7);font-size:12px;padding:6px 0;margin-bottom:6px;opacity:.9}
.social{display:flex;gap:10px}
.social span{width:34px;height:34px;border:1.5px solid #fff;border-radius:50%;display:block}
.legal-bar{top:2905px;height:47px;background:#6e5c32;color:#eee;font-size:12px;display:flex;align-items:center;justify-content:center}
</style>
</head>
<body>

<header class="section site-header">
  <div class="brand">Lorvan Beauty</div>
  <nav class="main-nav">
    <a class="active" href="#">Home</a>
    <a href="#">About Us</a>
    <a href="#">Clinical Examinations</a>
    <a href="#">Products</a>
    <a href="#">Business</a>
    <a href="#">Contact</a>
    <div class="flags"><span style="background:#d52b1e"></span><span style="background:#1f3f8a"></span></div>
  </nav>
</header>

<section class="section hero">
  <div class="hero-photo" role="img" aria-label="Black and white photo of a woman applying mascara to her lashes"></div>
  <div class="hero-copy">
    <h1 class="heading">The promise of a <span>LONG LOOK</span></h1>
    <p class="body-text">Effectiveness, fast effect, or maybe high quality? These are just some of the features that should make a GOOD EYELASH SERUM</p>
    <a class="btn" href="https://www.lorvanbeauty.shopnest.ch/">View Products</a>
  </div>
  <div class="slider-dots"><i class="on"></i><i></i><i></i><i></i></div>
  <svg class="hero-curve" width="1200" height="110" viewBox="0 0 1200 110">
    <path d="M0 110 L0 70 Q600 -20 1200 60 L1200 110 Z" fill="#fff"/>
    <path d="M0 72 Q600 -18 1200 62" fill="none" stroke="#b59c63" stroke-width="6"/>
  </svg>
</section>

<section class="section serum-intro">
  <div class="serum-portrait" role="img" aria-label="Round black and white portrait of a woman with a short blonde bob"></div>
  <div class="serum-copy">
    <h2 class="heading">Are you looking for the<br>best serum for your eyelashes?</h2>
    <p class="body-text">Effectiveness, fast effect, or maybe high quality? These are just some of the features that should make a GOOD EYELASH SERUM.<br>When using a particular product, we have high expectations for the product. REGENERATION FOR EYELASHES it should extend, make denser and nourish. It is also important to strengthen short and weak eyelashes.</p>
    <a class="btn" href="#">Learn More</a>
  </div>
</section>

<section class="section product-band band-gold">
  <div class="copy">
    <h2 class="heading">Aurelle Eyelash and Brow Conditioner</h2>
    <p class="body-text" style="color:#3a3a3a">Die Einzigartigen und Wirksamkeit des Produkts, die bereits nach 15 tägiger, regelmäßiger Anwendung bemerkbar werden, stellt ein Komplex von Substanzen, der sich gegenseitig ergänzt, sicher.</p>
    <a class="btn" href="#">Click here</a>
  </div>
  <div class="product-shot" style="left:760px;top:40px;width:290px;height:310px;background:linear-gradient(90deg,#111,#2e2e2e 60%,#0c0c0c)" role="img" aria-label="Black serum box beside a slim applicator tube"></div>
</section>

<section class="section product-band band-white">
  <div class="product-shot" style="left:170px;top:40px;width:330px;height:370px;background:linear-gradient(90deg,#fff,#d8d8d8 40%,#1a1a1a 55%,#e6e6e6 70%,#fff)" role="img" aria-label="Black mascara tubes with open wand brushes"></div>
  <div class="copy">
    <h2 class="heading">Velissa Volumizing Mascara</h2>
    <p class="label">INHALTSSTOFFE</p>
    <p class="body-text">Die Einzigartigen und Wirksamkeit des Produkts, die bereits nach 15 tägiger, regelmäßiger Anwendung bemerkbar werden, stellt ein Komplex von Substanzen, der sich gegenseitig ergänzt, sicher.</p>
    <a class="btn" href="#">Click here</a>
  </div>
</section>

<section class="section product-band band-grey">
  <div class="copy">
    <h2 class="heading">Serane Multitasking Hair Conditioner</h2>
    <p class="body-text">Die Einzigartigen und Wirksamkeit des Produkts, die bereits nach 15 tägiger, regelmäßiger Anwendung bemerkbar werden, stellt ein Komplex von Substanzen, der sich gegenseitig ergänzt, sicher.</p>
    <a class="btn" href="#">Click here</a>
  </div>
  <div class="product-shot" style="left:760px;top:35px;width:300px;height:380px;background:linear-gradient(180deg,#c9a85a 0%,#1a1a1a 30%,#262626 100%)" role="img" aria-label="Black foam bottle and black gift box tied with a gold ribbon"></div>
</section>

<section class="section newsletter">
  <h2 class="heading">Newsletter Sign Up</h2>
  <div class="subscribe-form">
    <svg width="18" height="14" viewBox="0 0 18 14"><rect x="1" y="1" width="16" height="12" fill="none" stroke="#555" stroke-width="1.5"/><path d="M1 1 L9 8 L17 1" fill="none" stroke="#555" stroke-width="1.5"/></svg>
    <span class="field">Email address</span>
    <span class="send">Subscribe</span>
  </div>
</section>

<footer class="section site-footer">
  <div class="footer-col">
    <h4>Quick Links</h4>
    <ul><li>Home</li><li>About Us</li><li>Clinical Examinations</li><li>Products</li></ul>
  </div>
  <div class="footer-col">
    <h4>Resources</h4>
    <ul><li>Business</li><li>Contact</li><li>Sitemap</li><li>Terms of Use</li></ul>
  </div>
  <div class="footer-col">
    <h4>Contact Us</h4>
    <div class="contact-field">Your name</div>
    <div class="contact-field">Email address</div>
    <div class="contact-field">Phone number</div>
  </div>
  <div class="footer-col">
    <h4>Follow Us</h4>
    <div class="social"><span></span><span></span><span></span><span></span></div>
  </div>
</footer>

<div class="section legal-bar">© 2018 Company Name. All rights reserved.</div>

</body>
</html>
```